Site for small consultancy for think tanks and non-profits

Small website to advertise consultancy. Description of services, copy about values, host page for podcast, contact details/email subscription, endorsements. Already have logo and two "house" colours. I need to be able to manage posting things on the website myself. Emphasis is on good quality advice and services, but at a value for money cost.

Target Market(s)

Market is global, but especially in emerging countries.

Industry/Entity Type

Non-Profit

Coding

Coded - Design and coding required

Number of Pages Required

5+ page

Font styles to use
Other font styles liked:
• Nordique Pro

Requirements
Must have
• Logo, and suitable use of the logo colours
Nice to have
• I'm not sure if the logo font is suitable for the whole website, but it should be featured in key areas.

```html
<!DOCTYPE html>
<html lang="en">
<head>
<meta charset="utf-8">
<title>Clearpath — Consultancy for think tanks and non-profits</title>
<link href="https://fonts.googleapis.com/css2?family=Hind:wght@400;500;600;700&family=Lato:wght@400;700&display=swap" rel="stylesheet">
<style>
:root{
  --plum-dark:#3a1750;
  --plum:#4a2166;
  --plum-deep:#42205e;
  --coral:#f4544a;
  --coral-text:#f05a4c;
  --ink:#1d1d22;
  --muted:#6c6c74;
  --light:#f2f2f2;
  --line:#e4e4e8;
  --footer:#2b2f34;
  --footer-bottom:#25282c;
  --star:#f7941d;
}
*{margin:0;padding:0;box-sizing:border-box}
html,body{width:1200px;height:2644px;overflow:hidden}
body{font-family:"Lato",sans-serif;color:var(--ink);background:#fff;position:relative}
h1,h2,h3,h4,.heading{font-family:"Hind",sans-serif}
.abs{position:absolute}
ul{list-style:none}

/* top bar */
.topbar{position:absolute;left:0;top:0;width:1200px;height:32px;background:var(--plum-dark);color:#fff;font-size:9px}
.topbar .welcome{position:absolute;left:235px;top:11px}
.topbar .mail{position:absolute;left:885px;top:11px;display:flex;align-items:center;gap:6px}

/* nav */
.nav{position:absolute;left:0;top:32px;width:1200px;height:50px;background:var(--plum)}
.brand{position:absolute;left:236px;top:8px;display:flex;align-items:center;gap:8px;color:#fff;font-family:"Hind",sans-serif;font-size:26px;font-weight:400;letter-spacing:.5px}
.brand .mark{width:10px;height:10px;background:var(--coral)}
.menu{position:absolute;left:400px;top:20px;display:flex;gap:30px;font-family:"Hind",sans-serif;font-size:10px;font-weight:600;color:#fff;letter-spacing:.3px}
.menu .active{color:var(--coral)}
.callbox{position:absolute;left:820px;top:0;width:380px;height:50px;background:#fff}
.callbox .badge{position:absolute;left:-11px;top:15px;width:22px;height:22px;border-radius:50%;background:var(--coral);display:flex;align-items:center;justify-content:center}
.callbox .label{position:absolute;left:25px;top:9px;font-family:"Hind",sans-serif;font-size:9px;font-weight:600;color:var(--plum)}
.callbox .num{position:absolute;left:23px;top:19px;font-family:"Hind",sans-serif;font-size:18px;font-weight:700;color:var(--plum)}

/* hero */
.hero{position:absolute;left:0;top:82px;width:1200px;height:456px;background:linear-gradient(100deg,#1f2b44 0%,#34456a 30%,#8b98b3 55%,#c9cfdc 75%,#b7bdca 100%)}
.hero-copy{position:absolute;left:235px;top:182px;color:#fff}
.hero-copy .light{font-family:"Hind",sans-serif;font-weight:400;font-size:38px;line-height:38px}
.hero-copy .bold{font-family:"Hind",sans-serif;font-weight:700;font-size:38px;line-height:40px}
.hero-copy p{font-size:11px;line-height:15px;width:340px;margin-top:14px}
.btn-coral{display:inline-block;background:var(--coral);color:#fff;font-family:"Hind",sans-serif;font-weight:600;font-size:9.5px;letter-spacing:.4px;padding:12px 23px 9px;margin-top:18px}

.callback{position:absolute;left:623px;top:46px;width:325px;height:363px;background:#fff;padding:22px 25px}
.callback h2{text-align:center;font-size:25px;font-weight:600;margin-bottom:20px}
.field{margin-top:12px}
.field label{display:block;font-family:"Hind",sans-serif;font-size:8px;font-weight:600;color:#6a6a72;letter-spacing:.5px;margin-bottom:5px}
.field .input{height:30px;background:var(--light);position:relative}
.field .caret{position:absolute;right:12px;top:13px;width:0;height:0;border-left:4px solid transparent;border-right:4px solid transparent;border-top:4px solid #666}
.submit{margin-top:20px;height:34px;border-radius:17px;background:var(--plum);color:#fff;font-family:"Hind",sans-serif;font-weight:600;font-size:12px;letter-spacing:.8px;display:flex;align-items:center;justify-content:center}

/* about & services */
.about{position:absolute;left:0;top:538px;width:549px;height:408px;background:var(--plum);color:#fff}
.about h2,.services h2{font-size:21px;font-weight:600;position:absolute;left:235px;top:68px}
.rule{position:absolute;width:44px;height:2px;background:var(--coral)}
.about .rule{left:236px;top:107px}
.about p{position:absolute;left:236px;top:130px;width:285px;font-size:9.2px;line-height:17.5px}
.btn-outline{position:absolute;left:235px;top:290px;width:102px;height:37px;border:1.5px solid #fff;font-family:"Hind",sans-serif;font-size:9.5px;font-weight:600;display:flex;align-items:center;justify-content:center;gap:14px}
.services{position:absolute;left:549px;top:538px;width:651px;height:408px;background:var(--light)}
.services h2{left:30px}
.services .rule{left:31px;top:107px}
.svc{position:absolute;width:180px}
.svc svg{position:absolute;left:0;top:0}
.svc h3{position:absolute;left:52px;top:0;font-size:14px;font-weight:600;line-height:18px}
.svc p{position:absolute;left:52px;top:44px;width:120px;font-size:8.3px;line-height:15px;color:#333}

/* projects */
.projects-title{position:absolute;left:0;top:1014px;width:1200px;text-align:center;font-size:20px;font-weight:600;letter-spacing:2px}
.grid{position:absolute;left:0;top:1078px;width:1200px;height:462px;display:grid;grid-template-columns:repeat(4,300px);grid-template-rows:231px 231px}
.tile{width:300px;height:231px}

/* help */
.help{position:absolute;left:0;top:1540px;width:1200px;height:303px;background:var(--plum-deep);color:#fff}
.help h2{position:absolute;top:50px;width:1200px;text-align:center;font-size:20px;font-weight:600;letter-spacing:1.6px}
.value{position:absolute;top:118px;width:180px;text-align:center}
.value svg{display:block;margin:0 auto}
.value h3{margin-top:28px;font-size:13.5px;font-weight:600}
.value p{margin-top:16px;font-size:9px;line-height:15px}

/* testimonials */
.testi-title{position:absolute;left:0;top:1905px;width:1200px;text-align:center;font-size:20px;font-weight:600;letter-spacing:1.6px}
.card{position:absolute;top:1967px;width:233px;height:183px;border:1px solid var(--line);padding:20px 20px}
.card .row{display:flex;justify-content:space-between;align-items:center}
.stars{display:flex;gap:5px}
.card p{margin-top:14px;font-size:8.7px;line-height:15px;color:#555}
.person{display:flex;align-items:center;gap:12px;margin-top:14px}
.avatar{width:48px;height:48px;border-radius:50%}
.person .name{font-family:"Hind",sans-serif;font-size:10.5px;font-weight:600}
.person .role{font-size:8.5px;color:#3a7bd5;margin-top:3px}
.pager{position:absolute;top:2196px;left:548px;display:flex;align-items:center;gap:10px}
.pager .arrow{width:26px;height:26px;border-radius:50%;border:1px solid #ddd;display:flex;align-items:center;justify-content:center}
.dot{width:5px;height:5px;border-radius:50%;background:#ccc}
.dot.on{background:var(--coral)}

/* newsletter */
.news{position:absolute;left:0;top:2279px;width:1200px;height:125px;background:var(--coral)}
.news .msg{position:absolute;left:264px;top:48px;display:flex;align-items:center;gap:10px;color:#fff;font-family:"Hind",sans-serif;font-size:13px;font-weight:600}
.news .form{position:absolute;left:633px;top:44px;width:333px;height:43px;border-radius:22px;background:#fff;border:2px solid #fff}
.news .form span{position:absolute;left:22px;top:15px;font-size:9px;color:#333}
.news .form .go{position:absolute;right:2px;top:2px;width:97px;height:35px;border-radius:18px;background:var(--plum);color:#fff;font-family:"Hind",sans-serif;font-size:9.5px;font-weight:600;display:flex;align-items:center;justify-content:center}

/* footer */
.footer{position:absolute;left:0;top:2404px;width:1200px;height:198px;background:var(--footer);color:#fff}
.footer h4{position:absolute;top:50px;font-size:10.5px;font-weight:600;letter-spacing:.3px}
.links{position:absolute;top:84px;font-size:8.5px;color:#cfd1d4}
.links li{margin-bottom:10px;display:flex;align-items:center;gap:9px}
.links li::before{content:"";width:3px;height:3px;background:#cfd1d4;border-radius:50%}
.divider{position:absolute;top:86px;width:1px;height:60px;background:#3f444a}
.ask{position:absolute;left:569px;top:83px;font-size:9px;line-height:13px;color:#cfd1d4}
.ask .k{color:var(--coral);font-weight:700}
.ask div+div{margin-top:11px}
.social{position:absolute;left:799px;top:91px;display:flex;gap:4px}
.social span{width:22px;height:22px;background:#3a3f45;border:1px solid #4a4f55}
.copy{position:absolute;left:0;top:2602px;width:1200px;height:42px;background:var(--footer-bottom);color:#b9bcc0;font-size:8px;text-align:center;padding-top:17px}
</style>
</head>
<body>

<div class="topbar">
  <span class="welcome">Welcome to Clearpath, we're here to help you</span>
  <span class="mail">
    <svg width="11" height="9" viewBox="0 0 11 9"><rect x=".5" y=".5" width="10" height="8" fill="none" stroke="#fff"/><path d="M.5 .5 5.5 5 10.5 .5" fill="none" stroke="#fff"/></svg>
    hello@clearpath-advisory.org
  </span>
</div>

<header class="nav">
  <div class="brand"><span>Clearpath</span><span class="mark"></span></div>
  <nav class="menu">
    <span class="active">HOME</span><span>ABOUT</span><span>SERVICES</span><span>TEAM</span><span>BLOG</span><span>CONTACT US</span>
  </nav>
  <div class="callbox">
    <span class="badge"><svg width="11" height="11" viewBox="0 0 24 24"><path d="M6.6 10.8a15 15 0 0 0 6.6 6.6l2.2-2.2a1 1 0 0 1 1-.25 11.4 11.4 0 0 0 3.6.57 1 1 0 0 1 1 1V20a1 1 0 0 1-1 1A17 17 0 0 1 3 4a1 1 0 0 1 1-1h3.5a1 1 0 0 1 1 1c0 1.25.2 2.45.57 3.57a1 1 0 0 1-.25 1z" fill="#fff"/></svg></span>
    <span class="label">Call Us:</span>
    <span class="num">(555) 014-2278</span>
  </div>
</header>

<section class="hero" role="img" aria-label="Photo of two smiling consultants in suits discussing a document at a desk">
  <div class="hero-copy">
    <div class="light">Grow your</div>
    <div class="bold">Business with us!!</div>
    <p>Lorem ipsum dolor sit amet, consectetur adipiscing elit. Sed eget justo consectetur, feugiat sem imperdiet, sagittis orci.</p>
    <span class="btn-coral">CONTACT US</span>
  </div>
  <form class="callback">
    <h2>Request Call Back</h2>
    <div class="field"><label>NAME</label><div class="input"></div></div>
    <div class="field"><label>EMAIL</label><div class="input"></div></div>
    <div class="field"><label>MOBILE(USED AS PASSWORD)</label><div class="input"></div></div>
    <div class="field"><label>AGENCY EMPLOYEES</label><div class="input"><span class="caret"></span></div></div>
    <div class="submit">SUBMIT</div>
  </form>
</section>

<section class="about">
  <h2>ABOUT US</h2>
  <span class="rule"></span>
  <p>Lorem ipsum dolor sit amet, consectetur adipiscing elit. Sed eget quam auctor, faucibus nisi eget, vehicula sapien. Vivamus sit amet efficitur eros, id scelerisque ante. Praesent fringilla enim ac libero condimentum aliquam. Phasellus felis massa, euismod eget metus sit amet, consequat tempor massa. Donec lobortis ipsum dolor, quis rhoncus enim commodo vel. Duis a iaculis nisi. Duis purus leo, cursus in congue nec, placerat non urna. Curabitur pharetra fermentum scelerisque. Suspendisse posuere dapibus sodales.</p>
  <span class="btn-outline">Read More
    <svg width="11" height="8" viewBox="0 0 11 8"><path d="M0 4h10M7 1l3 3-3 3" fill="none" stroke="#fff" stroke-width="1.2"/></svg>
  </span>
</section>

<section class="services">
  <h2>SERVICES</h2>
  <span class="rule"></span>
  <div class="svc" style="left:29px;top:156px">
    <svg width="40" height="40" viewBox="0 0 40 40"><circle cx="20" cy="11" r="8" fill="none" stroke="#f4544a" stroke-width="2.5"/><circle cx="7" cy="30" r="4" fill="#f4544a"/><circle cx="20" cy="30" r="4" fill="#f4544a"/><circle cx="33" cy="30" r="4" fill="#f4544a"/><rect x="2" y="35" width="36" height="4" fill="#f4544a"/></svg>
    <h3>Business<br>Consulting</h3>
    <p>Lorem ipsum dolor sit amet, consectetur adipiscing elit.</p>
  </div>
  <div class="svc" style="left:230px;top:156px">
    <svg width="40" height="40" viewBox="0 0 40 40"><rect x="4" y="28" width="5" height="10" fill="#f4544a"/><rect x="12" y="24" width="5" height="14" fill="#f4544a"/><rect x="20" y="20" width="5" height="18" fill="#f4544a"/><rect x="28" y="14" width="5" height="24" fill="#f4544a"/><path d="M3 22 15 14l7 4L36 6" fill="none" stroke="#f4544a" stroke-width="2.5"/><path d="M30 5h7v7" fill="none" stroke="#f4544a" stroke-width="2.5"/></svg>
    <h3>Financial<br>Analysis</h3>
    <p>Lorem ipsum dolor sit amet, consectetur adipiscing elit.</p>
  </div>
  <div class="svc" style="left:29px;top:265px">
    <svg width="40" height="40" viewBox="0 0 40 40"><circle cx="20" cy="20" r="7" fill="none" stroke="#f4544a" stroke-width="2.5"/><g fill="#f4544a"><circle cx="20" cy="4" r="3.5"/><circle cx="20" cy="36" r="3.5"/><circle cx="4" cy="20" r="3.5"/><circle cx="36" cy="20" r="3.5"/><circle cx="9" cy="9" r="3"/><circle cx="31" cy="9" r="3"/><circle cx="9" cy="31" r="3"/><circle cx="31" cy="31" r="3"/></g></svg>
    <h3>Business<br>Coaching</h3>
    <p>Lorem ipsum dolor sit amet, consectetur adipiscing elit.</p>
  </div>
  <div class="svc" style="left:230px;top:265px">
    <svg width="40" height="40" viewBox="0 0 40 40"><rect x="14" y="3" width="24" height="18" fill="none" stroke="#f4544a" stroke-width="2.5"/><path d="M18 17l5-5 4 3 7-7" fill="none" stroke="#f4544a" stroke-width="2"/><circle cx="8" cy="12" r="4.5" fill="#f4544a"/><rect x="3" y="18" width="10" height="20" fill="#f4544a"/><rect x="17" y="28" width="20" height="3" fill="#f4544a"/></svg>
    <h3>Business<br>Grow</h3>
    <p>Lorem ipsum dolor sit amet, consectetur adipiscing elit.</p>
  </div>
</section>

<h2 class="projects-title">OUR PROJECTS</h2>
<div class="grid">
  <div class="tile" role="img" aria-label="Overhead photo of a team meeting around a wooden table with laptops" style="background:linear-gradient(135deg,#5a4a3e,#8a7a6a)"></div>
  <div class="tile" role="img" aria-label="Photo of a young team gathered around a chalk board on the floor" style="background:linear-gradient(135deg,#c9c4bd,#4f8a8a)"></div>
  <div class="tile" role="img" aria-label="Group photo of a diverse team standing together" style="background:linear-gradient(135deg,#d8d6d2,#8e7e72)"></div>
  <div class="tile" role="img" aria-label="Photo of a man working on a laptop at a bright desk" style="background:linear-gradient(135deg,#6c6f78,#e9eaec)"></div>
  <div class="tile" role="img" aria-label="Photo of an office trading floor with screens" style="background:linear-gradient(135deg,#2d3d5a,#56698a)"></div>
  <div class="tile" role="img" aria-label="Photo of an audience watching a presentation in a meeting room" style="background:linear-gradient(135deg,#c8c3bc,#5b4d48)"></div>
  <div class="tile" role="img" aria-label="Photo of a team discussing around a conference table" style="background:linear-gradient(135deg,#6f6560,#d4d0cb)"></div>
  <div class="tile" role="img" aria-label="Overhead photo of hands working on paper plans on a white table" style="background:linear-gradient(135deg,#f3f3f3,#d9c7b8)"></div>
</div>

<section class="help">
  <h2>WE ARE ALWAYS HERE TO HELP!</h2>
  <div class="value" style="left:228px">
    <svg width="38" height="40" viewBox="0 0 38 40"><circle cx="19" cy="15" r="11" fill="none" stroke="#f4544a" stroke-width="2.5"/><circle cx="19" cy="15" r="5" fill="none" stroke="#f4544a" stroke-width="2"/><path d="M11 24 6 37l6-2 3 5 4-10M27 24l5 13-6-2-3 5-4-10" fill="none" stroke="#f4544a" stroke-width="2.2" stroke-linejoin="round"/></svg>
    <h3>Experienced</h3>
    <p>We have over 20 years experience providing expert financial advice.</p>
  </div>
  <div class="value" style="left:415px">
    <svg width="40" height="40" viewBox="0 0 40 40"><rect x="2" y="3" width="36" height="13" fill="none" stroke="#f4544a" stroke-width="2.5"/><rect x="14" y="7" width="12" height="5" fill="#f4544a"/><circle cx="10" cy="24" r="4" fill="none" stroke="#f4544a" stroke-width="2.2"/><circle cx="30" cy="24" r="4" fill="none" stroke="#f4544a" stroke-width="2.2"/><path d="M3 38c0-6 3-8 7-8s7 2 7 8M23 38c0-6 3-8 7-8s7 2 7 8" fill="none" stroke="#f4544a" stroke-width="2.2"/></svg>
    <h3>Trusted</h3>
    <p>A young, enthusiastic team of professionals are always here to help.</p>
  </div>
  <div class="value" style="left:604px">
    <svg width="38" height="40" viewBox="0 0 38 40"><circle cx="19" cy="12" r="9" fill="none" stroke="#f4544a" stroke-width="2.5"/><path d="M3 39c0-10 7-16 16-16s16 6 16 16" fill="none" stroke="#f4544a" stroke-width="2.5"/></svg>
    <h3>Professional</h3>
    <p>Our best specialists of insurance guarantee you will be protected.</p>
  </div>
  <div class="value" style="left:791px;width:185px">
    <svg width="40" height="40" viewBox="0 0 40 40"><path d="M9 6 14 11l-3 4a22 22 0 0 0 12 12l4-3 5 5-4 5C15 34 4 22 4 10z" fill="none" stroke="#f4544a" stroke-width="2.5" stroke-linejoin="round"/><path d="M24 6a10 10 0 0 1 10 10" fill="none" stroke="#f4544a" stroke-width="2.2"/><path d="M22 2l4 4-4 4" fill="none" stroke="#f4544a" stroke-width="2.2"/></svg>
    <h3>24/7 Available</h3>
    <p>Our professional and enthusiastic staff is always ready at your service 24/7.</p>
  </div>
</section>

<h2 class="testi-title">TESTIMONIALS FROM HAPPY CLIENTS</h2>

<article class="card" style="left:235px">
  <div class="row">
    <svg width="13" height="9" viewBox="0 0 13 9"><path d="M0 9V4Q0 0 4 0v2Q2 2 2 4h3v5zM7 9V4q0-4 4-4v2q-2 0-2 2h3v5z" fill="#7fb0e6"/></svg>
    <span class="stars">
      <svg width="12" height="12" viewBox="0 0 24 24"><path d="M12 1l3.1 7 7.4.7-5.6 5 1.7 7.3L12 17.3 5.4 21l1.7-7.3-5.6-5 7.4-.7z" fill="#f7941d"/></svg>
      <svg width="12" height="12" viewBox="0 0 24 24"><path d="M12 1l3.1 7 7.4.7-5.6 5 1.7 7.3L12 17.3 5.4 21l1.7-7.3-5.6-5 7.4-.7z" fill="#f7941d"/></svg>
      <svg width="12" height="12" viewBox="0 0 24 24"><path d="M12 1l3.1 7 7.4.7-5.6 5 1.7 7.3L12 17.3 5.4 21l1.7-7.3-5.6-5 7.4-.7z" fill="#f7941d"/></svg>
      <svg width="12" height="12" viewBox="0 0 24 24"><path d="M12 1l3.1 7 7.4.7-5.6 5 1.7 7.3L12 17.3 5.4 21l1.7-7.3-5.6-5 7.4-.7z" fill="#f7941d"/></svg>
      <svg width="12" height="12" viewBox="0 0 24 24"><path d="M12 1l3.1 7 7.4.7-5.6 5 1.7 7.3L12 17.3 5.4 21l1.7-7.3-5.6-5 7.4-.7z" fill="#f7941d"/></svg>
    </span>
  </div>
  <p>Lorem ipsum dolor sit amet, consectetur adipiscing elit. Quisque iaculis elementum eleifend. Cras malesuada vitae enim id imperdiet. Vestibulum vestibulum egestas.</p>
  <div class="person"><span class="avatar" role="img" aria-label="Client portrait photo" style="background:linear-gradient(135deg,#c9b8a6,#5d6c80)"></span><div><div class="name">MARA ELLISON</div><div class="role">Client</div></div></div>
</article>

<article class="card" style="left:485px">
  <div class="row">
    <svg width="13" height="9" viewBox="0 0 13 9"><path d="M0 9V4Q0 0 4 0v2Q2 2 2 4h3v5zM7 9V4q0-4 4-4v2q-2 0-2 2h3v5z" fill="#7fb0e6"/></svg>
    <span class="stars">
      <svg width="12" height="12" viewBox="0 0 24 24"><path d="M12 1l3.1 7 7.4.7-5.6 5 1.7 7.3L12 17.3 5.4 21l1.7-7.3-5.6-5 7.4-.7z" fill="#f7941d"/></svg>
      <svg width="12" height="12" viewBox="0 0 24 24"><path d="M12 1l3.1 7 7.4.7-5.6 5 1.7 7.3L12 17.3 5.4 21l1.7-7.3-5.6-5 7.4-.7z" fill="#f7941d"/></svg>
      <svg width="12" height="12" viewBox="0 0 24 24"><path d="M12 1l3.1 7 7.4.7-5.6 5 1.7 7.3L12 17.3 5.4 21l1.7-7.3-5.6-5 7.4-.7z" fill="#f7941d"/></svg>
      <svg width="12" height="12" viewBox="0 0 24 24"><path d="M12 1l3.1 7 7.4.7-5.6 5 1.7 7.3L12 17.3 5.4 21l1.7-7.3-5.6-5 7.4-.7z" fill="#f7941d"/></svg>
      <svg width="12" height="12" viewBox="0 0 24 24"><path d="M12 1l3.1 7 7.4.7-5.6 5 1.7 7.3L12 17.3 5.4 21l1.7-7.3-5.6-5 7.4-.7z" fill="#f7941d"/></svg>
    </span>
  </div>
  <p>Lorem ipsum dolor sit amet, consectetur adipiscing elit. Quisque iaculis elementum eleifend. Cras malesuada vitae enim id imperdiet. Vestibulum vestibulum egestas.</p>
  <div class="person"><span class="avatar" role="img" aria-label="Client portrait photo" style="background:linear-gradient(135deg,#e2e2e4,#9da3ac)"></span><div><div class="name">MARA ELLISON</div><div class="role">Client</div></div></div>
</article>

<article class="card" style="left:735px">
  <div class="row">
    <svg width="13" height="9" viewBox="0 0 13 9"><path d="M0 9V4Q0 0 4 0v2Q2 2 2 4h3v5zM7 9V4q0-4 4-4v2q-2 0-2 2h3v5z" fill="#7fb0e6"/></svg>
    <span class="stars">
      <svg width="12" height="12" viewBox="0 0 24 24"><path d="M12 1l3.1 7 7.4.7-5.6 5 1.7 7.3L12 17.3 5.4 21l1.7-7.3-5.6-5 7.4-.7z" fill="#f7941d"/></svg>
      <svg width="12" height="12" viewBox="0 0 24 24"><path d="M12 1l3.1 7 7.4.7-5.6 5 1.7 7.3L12 17.3 5.4 21l1.7-7.3-5.6-5 7.4-.7z" fill="#f7941d"/></svg>
      <svg width="12" height="12" viewBox="0 0 24 24"><path d="M12 1l3.1 7 7.4.7-5.6 5 1.7 7.3L12 17.3 5.4 21l1.7-7.3-5.6-5 7.4-.7z" fill="#f7941d"/></svg>
      <svg width="12" height="12" viewBox="0 0 24 24"><path d="M12 1l3.1 7 7.4.7-5.6 5 1.7 7.3L12 17.3 5.4 21l1.7-7.3-5.6-5 7.4-.7z" fill="#f7941d"/></svg>
      <svg width="12" height="12" viewBox="0 0 24 24"><path d="M12 1l3.1 7 7.4.7-5.6 5 1.7 7.3L12 17.3 5.4 21l1.7-7.3-5.6-5 7.4-.7z" fill="#f7941d"/></svg>
    </span>
  </div>
  <p>Lorem ipsum dolor sit amet, consectetur adipiscing elit. Quisque iaculis elementum eleifend. Cras malesuada vitae enim id imperdiet. Vestibulum vestibulum egestas.</p>
  <div class="person"><span class="avatar" role="img" aria-label="Client portrait photo" style="background:linear-gradient(135deg,#8a6a4c,#d7b98f)"></span><div><div class="name">MARA ELLISON</div><div class="role">Client</div></div></div>
</article>

<div class="pager">
  <span class="arrow"><svg width="6" height="8" viewBox="0 0 6 8"><path d="M5 1 2 4l3 3" fill="none" stroke="#555" stroke-width="1.2"/></svg></span>
  <span class="dot" style="margin-left:14px"></span><span class="dot on"></span><span class="dot" style="margin-right:14px"></span>
  <span class="arrow"><svg width="6" height="8" viewBox="0 0 6 8"><path d="M1 1l3 3-3 3" fill="none" stroke="#555" stroke-width="1.2"/></svg></span>
</div>

<section class="news">
  <div class="msg">
    <svg width="22" height="26" viewBox="0 0 22 26"><path d="M1 1h13l7 7v17H1z M14 1v7h7" fill="none" stroke="#fff" stroke-width="1.6" stroke-linejoin="round"/></svg>
    Keep up to date — get updates with latest topics.
  </div>
  <div class="form"><span>your email address</span><span class="go">SIGN ME UP!</span></div>
</section>

<footer class="footer">
  <h4 style="left:234px">QUICK LINKS</h4>
  <ul class="links" style="left:236px"><li>Home</li><li>About</li><li>Services</li></ul>
  <ul class="links" style="left:376px"><li>Team</li><li>Blog</li><li>Contact us</li></ul>
  <span class="divider" style="left:498px"></span>
  <h4 style="left:568px">YOU'VE QUESTION?</h4>
  <div class="ask">
    <div><span class="k">Get a Quote</span><br>(555) 014-3390</div>
    <div><span class="k">Send Email</span><br>office@clearpath-advisory.org</div>
  </div>
  <span class="divider" style="left:733px"></span>
  <h4 style="left:798px">FOLLOW US</h4>
  <div class="social" aria-label="Social media links"><span></span><span></span><span></span><span></span></div>
</footer>
<div class="copy">Copyright © 2020 Clearpath. All rights reserved.</div>

</body>
</html>
```